Creative, Fun, Eye catching signage for new office - inspire and inform!

I am looking for a billboard sign, a smaller sign and a very small sign for parking spots. These will be located in our new office space. I have uploaded two logos, this way you can choose. I would love to see what it looks like with black behind the logo but am open to creative ideas. I would like the majority of the background to be black and/or white

1. Sign for over door – with five at the top like in the photo attached

The sign size is 2600mm (L) x 900mm (H)

Logo at the top then services to the right side
Social & Living Skills Programs
Support Workers
Respite/Supported Holidays
Exercise Physiology
Occupational Therapy
Speech Therapy
Psychology
Behavioural Therapy

I would like the design to tie in with the website and/or flyers/banners attached. Please also try and add 1800 527 930

2. Sign for glass roller door

745cm wide by 725cm high ( similar to what next door has without it saying parent )

Tallbrook Logo
Drop Off Zone

Smaller signs for parking spots
1000cm wide, 60cm high

Tallbrook logo Visitor Parking 24/7

I would like the design to be consistent across the three items so they work together but are not identical.

I have attached images showing what I am talking about in relation to the location of each sign.

Target Market(s)

Families, parents and people with disabilities

Industry/Entity Type

Disability and community service

Colors

Designer to choose colors to be used in the design.

Requirements
Must have
• White or black background - the logo and please use colours shown in the brochures and banners provided. Preferences are black white and yellow
Nice to have
• all of our services and website and/or 1800 527 930 on banner 1
Should not have
• I dont want it to be to busy please

```html
<!DOCTYPE html>
<html lang="en">
<head>
<meta charset="utf-8">
<title>Tallbrook Office Signage</title>
<link rel="stylesheet" href="https://fonts.googleapis.com/css2?family=Kumbh+Sans:wght@600;700;800&family=Source+Sans+3:wght@600;700&display=swap">
<style>
  :root {
    --ink: #000000;
    --paper: #ffffff;
    --sun: #ecd85b;
    --sun-bright: #fcd94a;
    --label: #1a1a1a;
  }
  * { box-sizing: border-box; margin: 0; padding: 0; }
  html, body { width: 1200px; height: 900px; overflow: hidden; background: var(--paper); }
  .canvas { position: relative; width: 1200px; height: 900px; font-family: "Kumbh Sans", sans-serif; }

  .spec-label {
    position: absolute;
    font-family: "Source Sans 3", sans-serif;
    font-weight: 700;
    font-size: 18px;
    color: var(--label);
    white-space: nowrap;
  }
  .spec-label--door { left: 0; width: 1200px; top: 21px; text-align: center; }
  .spec-label--roller { left: 65px; top: 471px; }
  .spec-label--parking { left: 451px; width: 695px; top: 605px; text-align: center; }

  .brand { position: absolute; display: flex; flex-direction: column; align-items: center; }
  .brand__dot { border-radius: 50%; background: var(--sun-bright); }
  .brand__name { color: var(--paper); font-weight: 800; line-height: 1; letter-spacing: 0.5px; }

  /* Over-door billboard */
  .door-sign { position: absolute; left: 49px; top: 55px; width: 1102px; height: 382px; background: var(--sun); overflow: hidden; }
  .door-sign__band { position: absolute; left: 0; top: 0; width: 1102px; height: 223px; }
  .door-sign__number {
    position: absolute; left: 161px; top: 43px; width: 116px; height: 116px;
    border-radius: 50%; background: var(--sun);
    display: flex; align-items: center; justify-content: center;
    font-family: "Source Sans 3", sans-serif; font-weight: 700; font-size: 108px; color: var(--ink); line-height: 1;
    padding-bottom: 6px;
  }
  .door-sign .brand { left: 351px; width: 400px; top: 27px; }
  .door-sign .brand__dot { width: 72px; height: 72px; margin-bottom: 20px; }
  .door-sign .brand__name { font-size: 82px; }
  .door-sign__services {
    position: absolute; left: 0; width: 1102px; top: 240px;
    text-align: center; font-weight: 600; font-size: 22.5px; line-height: 27px; color: var(--ink);
  }
  .door-sign__services .sep { margin: 0 8px; font-weight: 600; }
  .door-sign__phone {
    position: absolute; left: 0; width: 1102px; top: 332px;
    display: flex; align-items: center; justify-content: center; gap: 8px;
    font-weight: 700; font-size: 23px; color: var(--ink);
  }
  .door-sign__phone svg { width: 27px; height: 27px; }

  /* Glass roller door sign */
  .roller-sign { position: absolute; left: 49px; top: 506px; width: 369px; height: 359px; background: var(--sun); }
  .roller-sign__top { position: absolute; left: 0; top: 0; width: 369px; height: 194px; background: var(--ink); }
  .roller-sign .brand { left: 0; width: 369px; top: 36px; }
  .roller-sign .brand__dot { width: 52px; height: 52px; margin-bottom: 12px; }
  .roller-sign .brand__name { font-size: 54px; }
  .roller-sign__message {
    position: absolute; left: 0; width: 369px; top: 213px;
    text-align: center; font-family: "Source Sans 3", sans-serif; font-weight: 700;
    font-size: 66px; line-height: 60px; color: var(--ink); letter-spacing: -0.5px;
  }

  /* Parking strip */
  .parking-sign { position: absolute; left: 451px; top: 644px; width: 695px; height: 41px; display: flex; }
  .parking-sign__brand { width: 163px; height: 41px; background: var(--ink); position: relative; }
  .parking-sign .brand { left: 0; width: 163px; top: 5px; }
  .parking-sign .brand__dot { width: 14px; height: 14px; margin-bottom: 2px; }
  .parking-sign .brand__name { font-size: 17px; }
  .parking-sign__label {
    width: 369px; height: 41px; background: var(--sun);
    display: flex; align-items: center; justify-content: center;
    font-family: "Source Sans 3", sans-serif; font-weight: 700; font-size: 39px; color: var(--ink);
  }
  .parking-sign__hours {
    width: 163px; height: 41px; background: var(--ink);
    display: flex; align-items: center; justify-content: center;
    font-family: "Source Sans 3", sans-serif; font-weight: 700; font-size: 39px; color: var(--paper);
  }
</style>
</head>
<body>
<main class="canvas">

  <p class="spec-label spec-label--door">Sign for over door | 260x90cm</p>
  <section class="door-sign" aria-label="Over-door sign">
    <svg class="door-sign__band" viewBox="0 0 1102 223" preserveAspectRatio="none" aria-hidden="true">
      <path d="M0 0 H1102 V186 Q551 268 0 186 Z" fill="var(--ink)"/>
    </svg>
    <div class="door-sign__number">5</div>
    <div class="brand">
      <span class="brand__dot"></span>
      <span class="brand__name">Tallbrook</span>
    </div>
    <div class="door-sign__services">
      <p>Social &amp; Living Skills Programs<span class="sep">|</span>Support Workers<span class="sep">|</span>Respite/Supported Holidays</p>
      <p>Exercise Physiology<span class="sep">|</span>Occupational Therapy<span class="sep">|</span>Speech Therapy</p>
      <p>Psychology<span class="sep">|</span>Behavioural Therapy</p>
    </div>
    <p class="door-sign__phone">
      <svg viewBox="0 0 24 24" aria-hidden="true">
        <circle cx="12" cy="12" r="12" fill="var(--ink)"/>
        <path d="M8.2 5.6c.5-.3 1.1-.2 1.4.3l1.3 2.2c.3.5.2 1.1-.2 1.4l-.9.7c.6 1.4 1.7 2.6 3.1 3.3l.7-.9c.4-.4 1-.5 1.4-.2l2.2 1.3c.5.3.6.9.3 1.4l-.8 1.2c-.5.7-1.4 1-2.2.8-3.5-1-6.3-3.8-7.3-7.3-.2-.8.1-1.7.8-2.2z" fill="var(--sun)"/>
      </svg>
      1800 527 930
    </p>
  </section>

  <p class="spec-label spec-label--roller">Sign for glass roller door | 74,5x72,5cm</p>
  <section class="roller-sign" aria-label="Glass roller door sign">
    <div class="roller-sign__top"></div>
    <div class="brand">
      <span class="brand__dot"></span>
      <span class="brand__name">Tallbrook</span>
    </div>
    <p class="roller-sign__message">DROP OFF<br>ZONE</p>
  </section>

  <p class="spec-label spec-label--parking">Smaller signs for parking spots | 100x6cm</p>
  <section class="parking-sign" aria-label="Parking spot sign">
    <div class="parking-sign__brand">
      <div class="brand">
        <span class="brand__dot"></span>
        <span class="brand__name">Tallbrook</span>
      </div>
    </div>
    <div class="parking-sign__label">VISITOR PARKING</div>
    <div class="parking-sign__hours">24/7</div>
  </section>

</main>
</body>
</html>
```